Web site design for Brivolt Software (www.brivoltsoftware-example.com)

Need the design as well as the html for the website. The brief is given in the attached file.
If possible, would like to use pencil sketches instead of images to give a unique look to the site.
Target Market(s)
small Software product companies
Industry/Entity Type
Software
Coding
Coded - Design and coding required
Number of Pages Required
5+ page

```html
<!DOCTYPE html>
<html lang="en">
<head>
<meta charset="utf-8">
<title>Brivolt Software</title>
<link rel="stylesheet" href="https://fonts.googleapis.com/css2?family=Kalam:wght@300;400&family=Open+Sans:wght@400;600;700&display=swap">
<style>
:root{
  --ink:#2b2b2b;
  --muted:#666;
  --soft:#8a8a8a;
  --gray:#e3e3e3;
  --light:#efefef;
  --white:#f8f8f8;
  --line:#cfcfcf;
  --sidebar:#ffffff;
}
*{box-sizing:border-box;margin:0;padding:0}
html,body{width:1200px;height:5248px;overflow:hidden;background:var(--white);color:var(--ink);font-family:"Open Sans",sans-serif}
.sidebar{position:absolute;left:0;top:0;width:322px;height:5248px;background:var(--sidebar)}
.brand{position:absolute;left:30px;top:24px;font-family:"Open Sans",sans-serif;font-weight:700;font-size:26px;letter-spacing:2px;color:var(--ink)}
.nav{position:absolute;left:30px;top:88px;list-style:none}
.nav li{font-family:"Kalam",cursive;font-size:20px;height:56px;line-height:56px;color:var(--ink)}
.nav li::before{content:"›";margin-right:10px}
.nav li.current{color:var(--soft);font-style:italic}
.legal{position:absolute;left:30px;top:5066px;font-size:12px;line-height:20px;color:var(--muted)}
.social{position:absolute;left:30px;top:5140px;display:flex;gap:18px}
.social span{width:24px;height:24px;border:2px solid var(--ink);border-radius:50%}
.main{position:absolute;left:322px;top:0;width:878px}
section{position:relative;width:878px;text-align:center}
.gray{background:var(--gray)}.light{background:var(--light)}.white{background:var(--white)}
h2{font-family:"Kalam",cursive;font-weight:400;font-size:36px;color:var(--ink)}
p{font-size:12px;line-height:19px;color:var(--muted)}
.hero{height:623px;background:linear-gradient(120deg,#fafafa,#dedede)}
.welcome{height:532px;padding:80px 80px 0}
.quote{font-family:"Kalam",cursive;font-size:22px;line-height:30px;margin:28px 30px 26px;color:var(--ink)}
.welcome p{margin-bottom:10px}
.clients{height:203px;padding-top:32px}
.clients h3,.small-h{font-size:12px;font-weight:400;color:var(--muted)}
.logos{display:flex;justify-content:space-between;padding:46px 60px 0}
.logos span{font-weight:700;font-size:16px;color:var(--ink)}
.split{display:flex;align-items:center;text-align:left;padding:0 70px;gap:50px}
.split h2{margin-bottom:16px}
.btn{display:inline-block;margin-top:20px;padding:8px 20px;border:1px solid var(--line);background:#fff;font-size:11px;color:var(--muted)}
.sketch{flex:none;border-radius:6px}
.cols{display:flex;justify-content:space-around;padding:0 40px}
.col{width:240px}
.col h4{font-family:"Kalam",cursive;font-weight:400;font-size:18px;margin:14px 0 8px}
.col .more{display:block;margin-top:14px;font-size:10px;text-decoration:underline;color:var(--ink)}
.dots{display:flex;justify-content:center;gap:12px;margin-top:40px}
.dots i{width:9px;height:9px;border-radius:50%;background:#bbb}
.dots i.on{background:var(--ink)}
.bubble{margin:34px 70px 0;border:3px solid var(--ink);border-radius:14px;padding:28px 40px 20px;background:#fafafa;text-align:left}
.bubble p{font-family:"Kalam",cursive;font-size:19px;line-height:28px;color:var(--ink)}
.cite{text-align:right;font-family:"Kalam",cursive;font-size:16px;margin:14px 80px 0}
.grid{display:grid;grid-template-columns:repeat(5,1fr);row-gap:60px;padding:50px 60px 0}
.grid span{font-weight:600;font-size:13px;color:var(--ink)}
.pagecount{position:absolute;right:12px;bottom:8px;font-size:10px}
</style>
</head>
<body>
<aside class="sidebar">
  <div class="brand">BRIVOLT</div>
  <ul class="nav">
    <li class="current">Home</li><li>Services</li><li>About US</li><li>Expertise</li><li>Engagement Models</li><li>Agile</li><li>Our Work</li><li>Work with us</li><li>Accolades</li><li>Stories</li><li>Winning Together</li><li>Giving back</li><li>Blog</li><li>Contact Us</li>
  </ul>
  <div class="legal">Copyright © 2017 Brivolt Software.<br>All rights reserved</div>
  <div class="social"><span></span><span></span><span></span><span></span><span></span></div>
</aside>

<main class="main">
  <section class="hero" role="img" aria-label="Pencil sketch of a light bulb beside hand-drawn charts and concept design notes, with a hand holding a pencil"></section>

  <section class="welcome gray">
    <h2>Welcome</h2>
    <div class="quote">"Perfection is achieved not when there is nothing more to add, but when there is nothing left to take away." —Lucien Marchetti</div>
    <p>Design pervades nature. Whether it is the unique symmetry of a snowflake, or the fibonacci number of a sunflower or nautilus shell, or self-replicating fractals, design is everywhere.</p>
    <p>In todays world, Good Design is associated more with tangible products, and User Interfaces. But good design has always been part of software engineering. Good design is what enables massive software millions to remain stable. Good design in UI and UX of course, but is also the process of deciding "what" is required, "how" it is to be built, "who" will build it, and how will its goodness perpetuate itself.</p>
    <p>We are a small but eclectic group of seasoned programmers who infuse rigor and design into solid engineering in software.</p>
    <p>We love to explore new frontiers in technology - be it Predictive Analytics, Cognitive, IOT or AI.</p>
    <p>We infuse design into rigorous engineering - not only in software design and UI, but also by using design thinking for deciding what to build, using design for designing the organizational structure of hierarchies, collaborations and communities; for designing the most productive work spaces and processes; and also communities which perpetuate and replicate themselves.</p>
  </section>

  <section class="clients light">
    <h3>Clients</h3>
    <div class="logos"><span>Tidewell</span><span>Surfrun</span><span>Coastline</span><span>Kelpstone</span><span>Nanoxo</span><span>Ramblefox</span></div>
  </section>

  <section class="white" style="height:340px;padding-top:78px">
    <div class="split">
      <svg width="110" height="120" viewBox="0 0 110 120" fill="none" stroke="#2b2b2b" stroke-width="4" aria-hidden="true"><circle cx="40" cy="45" r="26"/><circle cx="40" cy="45" r="9"/><circle cx="78" cy="88" r="20"/><circle cx="78" cy="88" r="7"/></svg>
      <div>
        <h2>Background and Expertise</h2>
        <p>We are primarily server side programmers with expertise in large scale projects - be it Software development tools, Distributed software frameworks, Telecom and mediation software or Business intelligence.</p>
        <span class="btn">Read more</span>
      </div>
    </div>
  </section>

  <section class="gray" style="height:490px;padding-top:62px">
    <h2>Services</h2>
    <div class="cols" style="margin-top:40px">
      <div class="col"><svg width="40" height="60" viewBox="0 0 40 60" fill="none" stroke="#2b2b2b" stroke-width="3"><rect x="4" y="2" width="32" height="56" rx="5"/><line x1="16" y1="50" x2="24" y2="50"/></svg><h4>POC</h4><p>Whether it is a mobile or web app prototype, or a more complex UI prototype, our engineers can understand the requirements.</p><span class="more">MORE</span></div>
      <div class="col"><svg width="60" height="60" viewBox="0 0 60 60" fill="none" stroke="#2b2b2b" stroke-width="4"><circle cx="30" cy="30" r="16" stroke-dasharray="6 4" stroke-width="8"/><circle cx="30" cy="30" r="6"/></svg><h4>Build Product</h4><p>Whether it is a mobile or web app prototype, or a more complex UI prototype, our engineers can understand the requirements.</p><span class="more">MORE</span></div>
      <div class="col"><svg width="60" height="60" viewBox="0 0 60 60" fill="none" stroke="#2b2b2b" stroke-width="5"><line x1="14" y1="14" x2="46" y2="46"/><circle cx="14" cy="14" r="8"/><line x1="46" y1="14" x2="14" y2="46"/></svg><h4>Maintain Product</h4><p>Whether it is a mobile or web app prototype, or a more complex UI prototype, our engineers can understand the requirements.</p><span class="more">MORE</span></div>
    </div>
    <div class="dots"><i class="on"></i><i></i><i></i><i></i></div>
  </section>

  <section class="white" style="height:308px;padding-top:70px">
    <div class="split">
      <div>
        <h2>About Us</h2>
        <p>We are seasoned programmers, interested in the science as well as the craft of programming.</p>
        <p style="margin-top:8px">We need to put high res black and white photos of our founders - followed by a paragraph about the team, their story and values.</p>
        <span class="btn">Read more</span>
      </div>
      <div class="sketch" role="img" aria-label="Pencil sketch of an open laptop" style="width:190px;height:140px;background:linear-gradient(#f0f0f0,#d6d6d6)"></div>
    </div>
  </section>

  <section class="gray" style="height:462px;padding-top:62px">
    <h2>Engagement Models</h2>
    <div class="cols" style="margin-top:26px;padding:0 120px">
      <div class="col" style="width:280px"><div role="img" aria-label="Sketch of a bar chart with a person" style="width:70px;height:60px;margin:auto;background:linear-gradient(#e9e9e9,#c9c9c9)"></div><h4>ODC</h4><p>We provide pure Outsourced product development for either new software development or product maintenance. Agile contracts and deliverable based compensation ensure value for customer and win-win.</p><span class="more">MORE</span></div>
      <div class="col" style="width:280px"><div role="img" aria-label="Sketch of a hand reaching to a globe" style="width:70px;height:60px;margin:auto;background:linear-gradient(#e9e9e9,#c9c9c9)"></div><h4>BOT</h4><p>We provide pure Outsourced product development for either new software development or product maintenance. Agile contracts and deliverable based compensation ensure value for customer and win-win.</p><span class="more">MORE</span></div>
    </div>
    <div class="dots" style="margin-top:50px"><i class="on"></i><i></i></div>
  </section>

  <section class="white" style="height:332px;padding-top:96px">
    <div class="split">
      <div class="sketch" role="img" aria-label="Pencil sketch of a stack of newspapers" style="width:160px;height:110px;background:linear-gradient(#dcdcdc,#b9b9b9)"></div>
      <div>
        <h2>Work with us</h2>
        <p>Brivolt works with startups and midsize product development companies. It uses design thinking and rigorous software development principles to build world class products.</p>
        <span class="btn">Read more</span>
      </div>
    </div>
  </section>

  <section class="gray" style="height:473px;padding-top:64px">
    <h2>Case Studies</h2>
    <div class="cols" style="margin-top:36px">
      <div class="col"><svg width="60" height="46" viewBox="0 0 60 46" fill="none" stroke="#2b2b2b" stroke-width="3"><path d="M30 8C20 2 10 2 3 6v36c7-4 17-4 27 2 10-6 20-6 27-2V6C50 2 40 2 30 8z"/><line x1="30" y1="8" x2="30" y2="44"/></svg><h4>Automation for vans - new product development</h4><span class="more">MORE</span></div>
      <div class="col"><svg width="60" height="46" viewBox="0 0 60 46" fill="none" stroke="#2b2b2b" stroke-width="3"><path d="M30 8C20 2 10 2 3 6v36c7-4 17-4 27 2 10-6 20-6 27-2V6C50 2 40 2 30 8z"/><line x1="30" y1="8" x2="30" y2="44"/></svg><h4>Data center asset tracking product - new product development</h4><span class="more">MORE</span></div>
      <div class="col"><svg width="60" height="46" viewBox="0 0 60 46" fill="none" stroke="#2b2b2b" stroke-width="3"><path d="M30 8C20 2 10 2 3 6v36c7-4 17-4 27 2 10-6 20-6 27-2V6C50 2 40 2 30 8z"/><line x1="30" y1="8" x2="30" y2="44"/></svg><h4>ERP system for almond manufacturers - new product development</h4><span class="more">MORE</span></div>
    </div>
    <div class="dots" style="margin-top:30px"><i class="on"></i><i></i><i></i><i></i></div>
  </section>

  <section class="white" style="height:385px;padding-top:66px">
    <h2>Accolades</h2>
    <div class="bubble"><p>“ Phasellus nisl est, condimentum vitae faucibus in, sollicitudin vel metus. Nunc sit amet consequat risus. Curabitur ac elit leo. In eleifend dui tellus, in scelerisque elit porttitor at. Integer eu massa lacinia, lacinia nulla non, volutpat purus.</p></div>
    <div class="cite">Jon Calder, City</div>
    <div class="dots" style="margin-top:22px"><i class="on"></i><i></i><i></i><i></i></div>
  </section>

  <section class="white" style="height:280px;padding-top:50px">
    <div class="split">
      <div>
        <h2>Giving Back</h2>
        <p>We believe in giving back in our own small way. Brivolt Software runs after the IT needs of Seven Lantern School.</p>
        <span class="btn">Read more</span>
      </div>
      <div class="sketch" role="img" aria-label="Pencil sketch of a large dollar sign" style="width:110px;height:170px;background:linear-gradient(#ededed,#cfcfcf)"></div>
    </div>
  </section>

  <section class="gray" style="height:350px;padding-top:58px">
    <h2>Partners</h2>
    <div class="grid"><span>Carvane</span><span>Fernhill</span><span>Lumora</span><span>Quillbay</span><span>Stonefold</span><span>Hollowell</span><span>Merrow</span><span>Brightmoor</span><span>Pendle</span><span>Arcadia</span></div>
  </section>

  <section class="light" style="height:470px;padding-top:66px">
    <h2>Blog</h2>
    <div class="cols" style="margin-top:34px">
      <div class="col"><svg width="44" height="46" viewBox="0 0 44 46" fill="none" stroke="#2b2b2b" stroke-width="3"><rect x="3" y="7" width="38" height="36" rx="3"/><line x1="3" y1="17" x2="41" y2="17"/><line x1="13" y1="2" x2="13" y2="11"/><line x1="31" y1="2" x2="31" y2="11"/></svg><h4>Aenean sed quam non sapien faucibus consequat vitae</h4><span class="more">MORE</span></div>
      <div class="col"><svg width="44" height="46" viewBox="0 0 44 46" fill="none" stroke="#2b2b2b" stroke-width="3"><rect x="3" y="7" width="38" height="36" rx="3"/><line x1="3" y1="17" x2="41" y2="17"/><line x1="13" y1="2" x2="13" y2="11"/><line x1="31" y1="2" x2="31" y2="11"/></svg><h4>Praesent quis risus mi. In mollis nulla in pulvinar dictum</h4><span class="more">MORE</span></div>
      <div class="col"><svg width="44" height="46" viewBox="0 0 44 46" fill="none" stroke="#2b2b2b" stroke-width="3"><rect x="3" y="7" width="38" height="36" rx="3"/><line x1="3" y1="17" x2="41" y2="17"/><line x1="13" y1="2" x2="13" y2="11"/><line x1="31" y1="2" x2="31" y2="11"/></svg><h4>Donec vestibulum odio sem, ac laoreet massa ullamcorper</h4><span class="more">MORE</span></div>
    </div>
    <div class="dots" style="margin-top:40px"><i class="on"></i><i></i><i></i><i></i></div>
    <span class="pagecount">BG</span>
  </section>
</main>
</body>
</html>
```